KVRD Pinecrest Rehabilitation Consultants, INC
Business Card and Stationary for KVRD Pinecrest Rehabilitation
Professional
Dorian K. Lumbard, Ph. D.
Vocational Rehabilitation Consultant
4173b GA Hwy 508 STE 612 Conyers, GA 30081
Dorian.Lumbard@kvrdpinecrestrehab.example
www.kvrdpinecrestrehab.example
I will need whole set of stationary, letterhead, envelopes etc.

```html
<!DOCTYPE html>
<html lang="en">
<head>
<meta charset="utf-8">
<title>KVRD Pinecrest Rehabilitation – Business Card</title>
<link href="https://fonts.googleapis.com/css2?family=Open+Sans:wght@400;600;700&display=swap" rel="stylesheet">
<style>
  :root {
    --backdrop: #e4e4e4;
    --card: #ffffff;
    --brand-blue: #1f5fa8;
    --ink-grey: #6b6b6b;
  }
  * { margin: 0; padding: 0; box-sizing: border-box; }
  html, body {
    width: 1200px; height: 902px; overflow: hidden;
    background: var(--backdrop);
    font-family: "Open Sans", sans-serif;
  }
  .stage { position: relative; width: 1200px; height: 902px; }
  .card {
    position: absolute;
    width: 560px; height: 320px;
    background: var(--card);
    box-shadow: 0 6px 18px rgba(0,0,0,0.18);
  }
  .card--back { left: 110px; top: 90px; }
  .card--front { left: 530px; top: 492px; }

  .contact {
    position: absolute; right: 34px; top: 36px;
    text-align: right; font-size: 12px; line-height: 19px;
    color: var(--ink-grey);
  }
  .contact__line { display: flex; justify-content: flex-end; align-items: center; gap: 6px; }
  .contact__icon { width: 10px; height: 10px; fill: var(--brand-blue); }
  .website {
    position: absolute; left: 34px; bottom: 34px;
    font-size: 16px; letter-spacing: 2px; color: var(--ink-grey);
    white-space: nowrap;
  }
  .website strong { color: var(--brand-blue); font-weight: 700; }

  .holder {
    position: absolute; right: 34px; top: 120px; text-align: right;
  }
  .holder__name { font-size: 20px; font-weight: 700; color: var(--brand-blue); }
  .holder__role { font-size: 14px; color: var(--ink-grey); margin-top: 2px; }

  .brand {
    position: absolute; left: 34px; bottom: 34px;
    display: flex; align-items: center; gap: 10px;
  }
  .brand__dot { width: 40px; height: 40px; border-radius: 50%; background: var(--brand-blue); }
  .brand__name {
    font-size: 20px; font-weight: 600; color: var(--brand-blue);
    line-height: 1.15; max-width: 240px;
  }
</style>
</head>
<body>
<main class="stage">
  <section class="card card--back" aria-label="Card back">
    <div class="contact">
      <div class="contact__line">4173b GA Hwy 508 STE 612</div>
      <div class="contact__line">Conyers, GA 30081</div>
      <div class="contact__line">770.555.0147
        <svg class="contact__icon" viewBox="0 0 10 10" aria-hidden="true"><path d="M2 0.5h2l1 2.5-1.3 1a5 5 0 0 0 2.3 2.3l1-1.3 2.5 1v2a1 1 0 0 1-1 1A8 8 0 0 1 1 1.5a1 1 0 0 1 1-1z"/></svg>
      </div>
      <div class="contact__line">Dorian.Lumbard@kvrdpinecrestrehab.example
        <svg class="contact__icon" viewBox="0 0 10 10" aria-hidden="true"><rect x="0" y="2" width="10" height="7"/></svg>
      </div>
    </div>
    <div class="website">www.<strong>kvrdpinecrestrehab</strong>.example</div>
  </section>

  <section class="card card--front" aria-label="Card front">
    <div class="holder">
      <div class="holder__name">Dorian K. Lumbard, Ph. D.</div>
      <div class="holder__role">Vocational Rehabilitation Consultant</div>
    </div>
    <div class="brand">
      <span class="brand__dot" aria-hidden="true"></span>
      <span class="brand__name">KVRD Pinecrest Rehabilitation</span>
    </div>
  </section>
</main>
</body>
</html>
```